Business Card Design Project : Tidewell Press

In preparation for market launch, Whistler's Tidewell Press require the development of a business card. Tidewell Press is a Community online publishing web portal. We provide the the city of Whistler located in B.C. (Canada) business directories, News, Classified ads, News, Events and blogs etc.

The main focus of the brand is to help local businesses to corporate with their online advertisement and marketing. Meeting our clients face to face is a must (B2B).

Target Market(s)

The target market is B2B customers. Business Owners to Marketing, advertising Managers

Industry/Entity Type

Business

Requirements
Must have
• - The business card will be two sided.
the BACK side will have our logo which consist of (icon, url,slogan) submited. The logo will be middle and centred.

The FRONT side should have company details:

Company Legal Name: FERNDALE TIDEWELL PRESS

Owen Marsk
Director of Sales & Marketing

www.ferndaletidewell.biz
owen@ferndaletidewell.biz

Phone: 555 014 3826
#2817 - 562 E. Harlow Ave.
Vancouver, B.C. K7P2R4 Canada
Nice to have
• - For the "FRONT" side of our business card. You can separate or re-arrange with our logo components (icon, logo,slogan). It does not have to be together.

Also our company legal name is rather long so arrange or organize the name in a way to make it shorter. Your experience and creativity will have to come in play.
Should not have
• should not have other colors beside logo color and black text (2 colors). Also nothing Three dimensional

```html
<!DOCTYPE html>
<html lang="en">
<head>
<meta charset="utf-8">
<title>Tidewell Press – Business Card</title>
<link rel="stylesheet" href="https://fonts.googleapis.com/css2?family=Open+Sans:wght@400;600&family=Roboto:wght@400;500;700;900&display=swap">
<style>
  :root {
    --backdrop: #2b2b2b;
    --card: #ffffff;
    --brand-blue: #1a82c8;
    --ink: #4a4a4a;
    --ink-soft: #5c5c5c;
    --accent-grey: #6d6e70;
  }
  * { margin: 0; padding: 0; box-sizing: border-box; }
  html, body {
    width: 1200px; height: 748px; overflow: hidden;
    background: var(--backdrop);
  }
  .canvas { position: relative; width: 1200px; height: 748px; }
  .card {
    position: absolute;
    width: 477px; height: 283px;
    background: var(--card);
  }

  /* Back side: brand lockup, centred */
  .card--back { left: 216px; top: 98px; }
  .brand-lockup {
    position: absolute; inset: 0;
    display: flex; flex-direction: column; align-items: center; justify-content: center;
    gap: 6px;
  }
  .brand-lockup__name {
    display: flex; align-items: center; gap: 10px;
    font-family: "Open Sans", sans-serif; font-weight: 600;
    font-size: 26px; color: var(--brand-blue);
  }
  .brand-lockup__mark {
    width: 18px; height: 18px; background: var(--brand-blue);
  }
  .brand-lockup__slogan {
    font-family: "Open Sans", sans-serif; font-weight: 400;
    font-size: 14px; color: var(--brand-blue);
  }

  /* Front side: company details */
  .card--front { left: 511px; top: 383px; overflow: hidden; }
  .company-name {
    position: absolute; left: 253px; top: 56px;
    font-family: "Roboto", sans-serif; font-weight: 900;
    font-size: 27px; line-height: 1.02; letter-spacing: 0.2px;
    color: var(--brand-blue);
  }
  .corner-block {
    position: absolute; right: 0; bottom: 0;
    width: 150px; height: 70px; background: var(--accent-grey);
  }
  .contact {
    position: absolute; left: 33px; top: 150px;
    font-family: "Roboto", sans-serif; color: var(--ink-soft);
    font-size: 10.5px; line-height: 1.3;
  }
  .contact__name {
    font-weight: 700; font-size: 14px; color: var(--ink); line-height: 1.2;
  }
  .contact__title { margin-bottom: 10px; }
  .contact__lines { margin-bottom: 10px; }
</style>
</head>
<body>
  <main class="canvas">
    <section class="card card--back" aria-label="Card back">
      <div class="brand-lockup">
        <div class="brand-lockup__name"><span class="brand-lockup__mark"></span>Tidewell Press</div>
        <div class="brand-lockup__slogan">Your information gateway</div>
      </div>
    </section>

    <section class="card card--front" aria-label="Card front">
      <h1 class="company-name">FERNDALE<br>TIDEWELL<br>PRESS</h1>
      <div class="corner-block"></div>
      <address class="contact" style="font-style: normal;">
        <div class="contact__name">Owen Marsk</div>
        <div class="contact__title">Director of Sales &amp; Marketing</div>
        <div class="contact__lines">
          Phone: 555 014 3826<br>
          www.ferndaletidewell.biz<br>
          owen@ferndaletidewell.biz
        </div>
        <div>
          #2817 - 562 E. Harlow Ave.<br>
          Vancouver, B.C. K7P2R4 Canada
        </div>
      </address>
    </section>
  </main>
</body>
</html>
```